Packaging Tape Design for Retail / Ecommerce Company

We need a design for custom packing tape for our company. We would like to see two designs for the packaging tape. 1) with the word fragile attached 2) Similiar design without the fragileMinimum resolution is 300 .ppi 3" x 6" or 3" x 12" - If selected, request that font that are used be identified. Orla Hearth Logo and package - Nest Bright! is a tagline we use on documents and correspondence. Looking for a creative design.

Target Market(s)

Mid level to high end consumers

Industry/Entity Type

Retail

Font styles to use
Sans Serif

Requirements
Must have
• logo must be included
• Nest Bright! - must be included
• web address: orlahearth.com
Nice to have
• creativity

```html
<!DOCTYPE html>
<html lang="en">
<head>
<meta charset="utf-8">
<title>Orla Hearth — Packing Tape</title>
<link rel="stylesheet" href="https://fonts.googleapis.com/css2?family=Josefin+Sans:wght@300;400;600&display=swap">
<style>
  :root {
    --bg: #f5f4f2;
    --tape: #ffffff;
    --edge: #4a4a4a;
    --green: #6dbd63;
    --blue: #445a9a;
    --sage: #b9d8a9;
    --plum: #9e356a;
    --amber: #e3af52;
    --coral: #e24b3b;
    --maroon: #7d1a16;
    --ink: #222222;
  }
  html, body {
    margin: 0;
    padding: 0;
    width: 1200px;
    height: 1000px;
    overflow: hidden;
    background: var(--bg);
  }
  .canvas {
    width: 1200px;
    height: 1000px;
    display: flex;
    flex-direction: column;
    align-items: center;
    justify-content: center;
    gap: 64px;
  }
  .tape { display: block; }
  .tape-body { fill: var(--tape); stroke: var(--edge); stroke-width: 1; }
  .band-top { fill: url(#band-top-fill); }
  .band-bottom { fill: url(#band-bottom-fill); }
  .stop-sage { stop-color: var(--sage); }
  .stop-amber { stop-color: var(--amber); }
  .stop-coral { stop-color: var(--coral); }
  .stop-plum { stop-color: var(--plum); }
  .brand-name {
    font-family: "Josefin Sans", sans-serif;
    font-weight: 600;
    font-size: 21px;
    fill: var(--maroon);
  }
  .brand-mark { fill: var(--maroon); }
  .tagline {
    font-family: "Josefin Sans", sans-serif;
    font-weight: 300;
    font-size: 25px;
    letter-spacing: 4px;
    fill: var(--maroon);
  }
  .web-address {
    font-family: "Josefin Sans", sans-serif;
    font-weight: 400;
    font-size: 9.5px;
    letter-spacing: 0.3px;
    fill: var(--ink);
  }
  .fragile-backdrop { fill: var(--blue); }
  .fragile-icon { fill: none; stroke: var(--coral); stroke-width: 3; }
  .fragile-label {
    font-family: "Josefin Sans", sans-serif;
    font-weight: 400;
    font-size: 11px;
    fill: #ffffff;
  }
</style>
</head>
<body>
<main class="canvas">

  <svg width="0" height="0" style="position:absolute" aria-hidden="true">
    <defs>
      <linearGradient id="band-top-fill" x1="0" y1="0" x2="1" y2="0">
        <stop offset="0" class="stop-sage"/>
        <stop offset="1" class="stop-amber"/>
      </linearGradient>
      <linearGradient id="band-bottom-fill" x1="0" y1="0" x2="1" y2="0">
        <stop offset="0" class="stop-coral"/>
        <stop offset="1" class="stop-plum"/>
      </linearGradient>
    </defs>
  </svg>

  <!-- Tape: standard -->
  <svg class="tape tape-standard" width="947" height="272" viewBox="0 0 592 170">
    <rect class="tape-body" x="0.5" y="0.5" width="591" height="169"/>
    <rect class="band-top" x="169" y="1" width="422" height="61" role="img" aria-label="Multicolour block stripe pattern, upper band"/>
    <rect class="band-bottom" x="169" y="109" width="422" height="60" role="img" aria-label="Multicolour block stripe pattern, lower band"/>
    <g class="brand">
      <rect class="brand-mark" x="20" y="75" width="10" height="10"/>
      <text class="brand-name" x="36" y="88">Orla Hearth</text>
    </g>
    <text class="tagline" x="376" y="95" text-anchor="middle">NEST BRIGHT!</text>
    <text class="web-address" x="15" y="155">WWW.ORLAHEARTH.COM</text>
  </svg>

  <!-- Tape: fragile -->
  <svg class="tape tape-fragile" width="947" height="272" viewBox="0 0 592 170">
    <rect class="tape-body" x="0.5" y="0.5" width="591" height="169"/>
    <rect class="band-top" x="169" y="1" width="422" height="61" role="img" aria-label="Multicolour block stripe pattern, upper band"/>
    <rect class="band-bottom" x="169" y="109" width="422" height="60" role="img" aria-label="Multicolour block stripe pattern, lower band"/>
    <g class="fragile-badge">
      <rect class="fragile-backdrop" x="216" y="1" width="77" height="61"/>
      <polygon class="fragile-icon" points="254,6 228,55 280,55"/>
      <rect class="fragile-backdrop" x="224" y="25" width="60" height="16"/>
      <text class="fragile-label" x="254" y="38" text-anchor="middle">FRAGILE</text>
    </g>
    <g class="brand">
      <rect class="brand-mark" x="20" y="75" width="10" height="10"/>
      <text class="brand-name" x="36" y="88">Orla Hearth</text>
    </g>
    <text class="tagline" x="376" y="95" text-anchor="middle">NEST BRIGHT!</text>
    <text class="web-address" x="15" y="155">WWW.ORLAHEARTH.COM</text>
  </svg>

</main>
</body>
</html>
```